Wine label for premium wine of vinery Vrbolanec.

Design Premium wine label.

The brand is called Melvara. Brand can be extended to Dorano Melvara. There
The label should be unique and high class feeling.
This is facebook lonk of the winery
https://www.pagebook.example/402918365510274/

On facebook you can see some examole of labels that are used now. Winery is called Vrbolanec, so they used letter "K" as a logo in different ways

Target Market(s)

Premium high class yet modern living traditional but also gadget fun.
I have uploaded few inspirational photos that the owner of the vinery likes. Hope it helps.

Industry/Entity Type

Vinery

Requirements
Must have
• Black, gold, silver color to be dominated. Colors that are NOT acceptable are: green, yellow, blue, purple, pink.

The name of the vinary is Vrbolanec and it should be on the front label.
Nice to have
• The size of label should fit the Grapely application screenshot frame.
Should not have
• Cheap perception of the label and brand

```html
<!DOCTYPE html>
<html lang="en">
<head>
<meta charset="utf-8">
<title>Vrbolanec Melvara 2015 – Wine Label</title>
<link rel="stylesheet" href="https://fonts.googleapis.com/css2?family=EB+Garamond:wght@400&family=Roboto:wght@500;700&family=Great+Vibes&display=swap">
<style>
  :root {
    --page: #ffffff;
    --stage: #f7f7f7;
    --band: #e6e6e6;
    --label-black: #050505;
    --gold: #a8832e;
    --gold-mid: #7d6024;
    --gold-deep: #3a2c10;
    --silver: #d9d9d9;
    --silver-bright: #f4f4f4;
  }
  * { margin: 0; padding: 0; box-sizing: border-box; }
  html, body { width: 1200px; height: 1000px; overflow: hidden; background: var(--page); }
  .canvas { position: relative; width: 1200px; height: 1000px; background: var(--page); }
  .stage {
    position: absolute; left: 0; top: 160px; width: 1200px; height: 696px;
    background: radial-gradient(ellipse at center, #ffffff 40%, var(--stage) 100%);
  }
  .stage-band { position: absolute; left: 0; width: 1200px; height: 28px; background: var(--band); }
  .stage-band.top { top: 0; }
  .stage-band.bottom { bottom: 0; height: 32px; }

  .wine-label {
    position: absolute; left: 404px; top: 262px; width: 385px; height: 499px;
    background: var(--label-black); overflow: hidden;
  }
  .label-frame {
    position: absolute; inset: 8px; border-radius: 26px;
    border: 4px solid var(--gold);
  }
  .ornament-field {
    position: absolute; inset: 14px; border-radius: 21px;
    background:
      radial-gradient(ellipse 44% 26% at 52% 46%, var(--label-black) 45%, rgba(5,5,5,0.85) 70%, rgba(5,5,5,0) 100%),
      linear-gradient(180deg, var(--gold-mid) 0%, var(--gold-deep) 30%, var(--gold-deep) 70%, var(--gold-mid) 100%),
      var(--gold-deep);
    background-blend-mode: normal;
  }
  .ornament-field::after {
    content: ""; position: absolute; inset: 0; border-radius: inherit;
    background:
      linear-gradient(90deg, rgba(168,131,46,0.55) 0%, rgba(168,131,46,0) 22%, rgba(168,131,46,0) 78%, rgba(168,131,46,0.55) 100%);
  }
  .label-text { position: absolute; left: 0; right: 0; text-align: center; z-index: 2; }
  .winery-name {
    top: 116px; font-family: "EB Garamond", serif; font-size: 25px;
    color: var(--silver); letter-spacing: 0.5px;
  }
  .origin {
    top: 159px; font-family: "Roboto", sans-serif; font-weight: 500; font-size: 17px;
    color: var(--gold); letter-spacing: 3px;
  }
  .vintage {
    top: 179px; font-family: "Roboto", sans-serif; font-weight: 700; font-size: 19px;
    color: var(--silver); letter-spacing: 2px;
  }
  .wine-name {
    top: 198px; left: 44px; right: 24px;
    font-family: "Great Vibes", cursive; font-size: 84px; line-height: 1;
    color: var(--silver-bright);
    transform: rotate(-12deg); transform-origin: center;
  }
</style>
</head>
<body>
<div class="canvas">
  <div class="stage">
    <div class="stage-band top"></div>
    <div class="stage-band bottom"></div>
  </div>

  <section class="wine-label">
    <div class="ornament-field" role="img" aria-label="Gold baroque scrollwork and acanthus ornament filling the label around a black central panel, on an etched black ground"></div>
    <div class="label-frame"></div>
    <p class="label-text winery-name">VRBOLANEC</p>
    <p class="label-text origin">CROATIA</p>
    <p class="label-text vintage">2015</p>
    <p class="label-text wine-name">Melvara</p>
  </section>
</div>
</body>
</html>
```